A Speech Therapy Business needs to update their logo

I need an update to the font and color of my logo to look more appealing. I am looking to open a private practice as a Speech Language Pathologist that caters to adults and children. It needs to be sophisticated and friendly at the same time. I want to keep the silhouette in my logo as is, just update the font and color for "Brightpath".
Industry/Entity Type
Business
Contact Information for Business Card
I want the business card to have my logo, my name (Odile Varn, CCC-SLP, TSSLD) and that I am a Bilingual Speech Language Pathologist. Also, include my phone number, (718) 555-0193. Include my website, Brightpathslp.example, and email address, odilevarn@brightpathslp.example
Look and feel

```html
<!DOCTYPE html>
<html lang="en">
<head>
<meta charset="utf-8">
<title>Brightpath Business Card</title>
<link href="https://fonts.googleapis.com/css2?family=Montserrat:wght@700&family=Raleway:wght@400;600&display=swap" rel="stylesheet">
<style>
  :root {
    --page: #e9e6e1;
    --card: #0c0c0d;
    --card-sheen: #232325;
    --accent: #1aa6dc;
    --text: #f2f2f2;
    --muted: #d6d6d6;
  }
  html, body {
    margin: 0;
    width: 1200px;
    height: 1022px;
    overflow: hidden;
    background: var(--page);
  }
  .card {
    position: absolute;
    left: 100px;
    top: 231px;
    width: 1000px;
    height: 560px;
    border-radius: 18px;
    overflow: hidden;
    background: radial-gradient(ellipse at 45% 45%, var(--card-sheen) 0%, var(--card) 60%);
    box-shadow: 0 18px 40px rgba(0,0,0,.25);
    font-family: "Raleway", sans-serif;
    color: var(--text);
  }
  .logo { position: absolute; left: 64px; top: 150px; }
  .logo-figures {
    width: 330px;
    height: 86px;
    background: linear-gradient(90deg, #ffffff 0%, #e6e6e6 100%);
    opacity: .92;
    border-radius: 4px;
  }
  .logo-name {
    margin-top: 14px;
    font-family: "Raleway", sans-serif;
    font-weight: 400;
    font-size: 50px;
    letter-spacing: 2px;
    color: var(--text);
    line-height: 1;
  }
  .contact {
    position: absolute;
    left: 64px;
    top: 392px;
    width: 440px;
    border-top: 2px solid var(--accent);
    padding-top: 14px;
  }
  .contact-row {
    display: flex;
    align-items: center;
    gap: 14px;
    font-size: 20px;
    line-height: 34px;
    color: var(--muted);
  }
  .contact-row svg { width: 16px; height: 16px; flex: none; }
  .contact-row strong { color: var(--accent); font-weight: 600; }
  .identity {
    position: absolute;
    right: 60px;
    top: 70px;
    width: 440px;
    text-align: right;
    border-bottom: 2px solid var(--accent);
    padding-bottom: 16px;
  }
  .identity-name {
    font-family: "Montserrat", sans-serif;
    font-weight: 700;
    font-size: 32px;
    letter-spacing: 1px;
    color: var(--accent);
    text-transform: uppercase;
  }
  .identity-credentials { font-size: 22px; margin-top: 4px; }
  .identity-title { font-size: 22px; margin-top: 40px; }
  .accent-band { position: absolute; left: 0; bottom: 0; }
</style>
</head>
<body>
  <div class="card">
    <div class="logo">
      <div class="logo-figures" role="img" aria-label="Logo silhouette of a family walking in a row, from adult to small child"></div>
      <div class="logo-name">BRIGHTPATH</div>
    </div>

    <div class="identity">
      <div class="identity-name">Odile Varn</div>
      <div class="identity-credentials">CCC-SLP, TSSLD</div>
      <div class="identity-title">Bilingual Speech Language Pathologist</div>
    </div>

    <div class="contact">
      <div class="contact-row">
        <svg viewBox="0 0 16 16"><path d="M4 1 L6.5 4 L5 6 C6 8.5 7.5 10 10 11 L12 9.5 L15 12 L13 15 C7 14.5 1.5 9 1 3 Z" fill="#1aa6dc"/></svg>
        (718) 555-0193
      </div>
      <div class="contact-row">
        <svg viewBox="0 0 16 16"><rect x="1" y="3" width="14" height="10" fill="none" stroke="#1aa6dc" stroke-width="1.6"/><path d="M1 3 L8 9 L15 3" fill="none" stroke="#1aa6dc" stroke-width="1.6"/></svg>
        odilevarn@brightpathslp.example
      </div>
      <div class="contact-row">
        <svg viewBox="0 0 16 16"><circle cx="8" cy="8" r="7" fill="none" stroke="#1aa6dc" stroke-width="1.5"/><path d="M1 8 H15 M8 1 C4 5 4 11 8 15 M8 1 C12 5 12 11 8 15" fill="none" stroke="#1aa6dc" stroke-width="1.2"/></svg>
        <span>www.<strong>brightpathslp</strong>.example</span>
      </div>
    </div>

    <svg class="accent-band" width="1000" height="80" viewBox="0 0 1000 80" aria-hidden="true">
      <path d="M560 80 L560 30 Q560 14 576 14 L640 14 Q652 14 656 26 L660 40 L1000 40 L1000 80 Z" fill="#1aa6dc"/>
    </svg>
  </div>
</body>
</html>
```